CPA Firm Business Card
Halvorin, Bestwick & Pardue CPAs, LLC
Project: CPA Firm Business Card
CPA Firm Business Card - Financial Services
Creative Brief
Professional
Moss Brandley, CPA
2867 E. Sable Way, Suite 348 Tucson, AZ 85619
moss@quillledger.net
In addition to business cards design I would also like to see designs for letterheads, envelopes and fax cover sheets.

```html
<!DOCTYPE html>
<html lang="en">
<head>
<meta charset="utf-8">
<title>Halvorin, Bestwick &amp; Pardue CPAs, LLC — Business Card</title>
<link rel="stylesheet" href="https://fonts.googleapis.com/css2?family=Open+Sans:wght@400;600;700&display=swap">
<style>
  :root {
    --backdrop: #e9e6e2;
    --card-white: #ffffff;
    --firm-red: #7d1416;
    --rule-grey: #8a8a8a;
    --text-white: #ffffff;
  }
  html, body {
    margin: 0;
    padding: 0;
    width: 1200px;
    height: 900px;
    overflow: hidden;
    background: var(--backdrop);
    font-family: "Open Sans", Arial, sans-serif;
  }
  .stage {
    width: 1200px;
    height: 900px;
    display: flex;
    align-items: center;
    justify-content: center;
  }
  .business-card {
    position: relative;
    width: 1000px;
    height: 572px;
    background: var(--card-white);
    box-shadow: 0 10px 30px rgba(0,0,0,0.18);
    overflow: hidden;
  }
  .firm-mark {
    position: absolute;
    left: 190px;
    top: 92px;
    display: flex;
    align-items: flex-start;
    gap: 22px;
  }
  .firm-mark__square {
    width: 112px;
    height: 112px;
    background: var(--firm-red);
    margin-top: 6px;
  }
  .firm-mark__name {
    margin: 0;
    color: var(--firm-red);
    font-weight: 700;
    font-size: 38px;
    line-height: 36px;
    text-transform: uppercase;
    letter-spacing: -0.5px;
  }
  .firm-mark__name span { display: block; }
  .firm-mark__name .firm-mark__suffix {
    font-size: 17px;
    line-height: 22px;
    text-transform: none;
    text-align: right;
  }
  .firm-rule {
    position: absolute;
    left: 190px;
    top: 250px;
    width: 420px;
    height: 3px;
    background: var(--rule-grey);
  }
  .contact-band {
    position: absolute;
    left: 0;
    top: 318px;
    width: 100%;
    height: 200px;
    background: var(--firm-red);
  }
  .person-name {
    position: absolute;
    left: 44px;
    top: 80px;
    margin: 0;
    color: var(--text-white);
    font-weight: 600;
    font-size: 26px;
  }
  .contact-list {
    position: absolute;
    left: 588px;
    top: 20px;
    margin: 0;
    padding: 0;
    list-style: none;
    color: var(--text-white);
    font-size: 17px;
    line-height: 24px;
  }
  .contact-list li {
    display: flex;
    align-items: flex-start;
    gap: 10px;
  }
  .contact-list svg {
    flex: none;
    width: 18px;
    height: 18px;
    margin-top: 3px;
  }
  .contact-list .contact-list__plain { padding-left: 28px; }
</style>
</head>
<body>
<main class="stage">
  <article class="business-card">
    <div class="firm-mark">
      <div class="firm-mark__square"></div>
      <h1 class="firm-mark__name">
        <span>Halvorin</span>
        <span>Bestwick &amp;</span>
        <span>Pardue</span>
        <span class="firm-mark__suffix">CPAs, LLC</span>
      </h1>
    </div>
    <div class="firm-rule"></div>

    <section class="contact-band">
      <p class="person-name">Moss Brandley, CPA</p>
      <ul class="contact-list">
        <li>
          <svg viewBox="0 0 18 18" aria-hidden="true"><circle cx="9" cy="9" r="9" fill="#fff"/><path d="M9 4 L4 8.5 H5.5 V13.5 H12.5 V8.5 H14 Z" fill="#7d1416"/></svg>
          <span>2867 E. Sable Way, Suite 348</span>
        </li>
        <li class="contact-list__plain">Tucson, AZ 85619</li>
        <li>
          <svg viewBox="0 0 18 18" aria-hidden="true"><circle cx="9" cy="9" r="9" fill="#fff"/><path d="M6 4.5 L8 4.5 L8.8 7 L7.6 8 Q8.6 10 10.2 10.6 L11.2 9.4 L13.5 10.2 L13.5 12.3 Q12.8 13.5 11 13.2 Q6 11.6 4.8 6.6 Q4.7 5 6 4.5 Z" fill="#7d1416"/></svg>
          <span>520-555-0147</span>
        </li>
        <li>
          <svg viewBox="0 0 18 18" aria-hidden="true"><circle cx="9" cy="9" r="9" fill="#fff"/><rect x="6.2" y="3.5" width="5.6" height="11" rx="1" fill="#7d1416"/><rect x="7.2" y="5" width="3.6" height="6.5" fill="#fff"/></svg>
          <span>520-555-0182</span>
        </li>
        <li>
          <svg viewBox="0 0 18 18" aria-hidden="true"><circle cx="9" cy="9" r="9" fill="#fff"/><rect x="4" y="5.5" width="10" height="7" fill="#7d1416"/><path d="M4 5.5 L9 9.5 L14 5.5" stroke="#fff" stroke-width="1" fill="none"/></svg>
          <span>moss@quillledger.net</span>
        </li>
        <li>
          <svg viewBox="0 0 18 18" aria-hidden="true"><circle cx="9" cy="9" r="9" fill="#fff"/><circle cx="9" cy="9" r="5" fill="none" stroke="#7d1416" stroke-width="1.3"/><path d="M4 9 H14 M9 4 Q6 9 9 14 M9 4 Q12 9 9 14" stroke="#7d1416" stroke-width="1" fill="none"/></svg>
          <span>www.quillledger.net</span>
        </li>
      </ul>
    </section>
  </article>
</main>
</body>
</html>
```